Business Card for Trivelo, a french tech company

Tech company
New technologies
Serious design
Dark theme

User info :
Name: Florian GASTIER
Position: Co-Founder & CEO
Tel: (+33) 6 52 84 26 07
Email: florian@trivelo.example
Website: www.trivelo.example
Address: 17 rue des Tanneurs 69001 LYON

```html
<!DOCTYPE html>
<html lang="fr">
<head>
<meta charset="utf-8">
<title>Trivelo — Business Card</title>
<link href="https://fonts.googleapis.com/css2?family=Montserrat:wght@400;500;600;700&display=swap" rel="stylesheet">
<style>
  :root {
    --canvas: #dcdcdc;
    --navy-top: #032d5e;
    --navy-bottom: #05003c;
    --ink: #120a40;
    --white: #ffffff;
    --magenta: #e3119c;
    --violet: #9b10e8;
    --radius: 31px;
  }
  * { margin: 0; padding: 0; box-sizing: border-box; }
  html, body {
    width: 1200px; height: 1200px; overflow: hidden;
    background: var(--canvas);
    font-family: "Montserrat", sans-serif;
  }
  .stage { position: relative; width: 1200px; height: 1200px; }

  .card {
    position: absolute; top: 227px;
    width: 448px; height: 746px;
    border-radius: var(--radius);
    overflow: hidden;
  }

  /* Back side */
  .card--back {
    left: 131px;
    background: linear-gradient(180deg, var(--navy-top) 0%, var(--navy-bottom) 100%);
  }
  .brand-vertical {
    position: absolute; left: 50%; top: 52%;
    transform: translate(-50%, -50%) rotate(-90deg);
    color: var(--white);
    font-weight: 700; font-size: 98px; letter-spacing: 4px;
    white-space: nowrap; line-height: 1;
  }

  /* Front side */
  .card--front {
    left: 633px;
    background: linear-gradient(180deg, var(--navy-top) 0%, var(--navy-bottom) 100%);
  }
  .front__brand-zone {
    position: absolute; left: 0; top: 0; width: 100%; height: 373px;
    background: var(--white);
    display: flex; align-items: center; justify-content: center; gap: 16px;
  }
  .brand-dot {
    width: 34px; height: 34px; border-radius: 50%;
    background: var(--ink);
  }
  .brand-name {
    color: var(--ink); font-weight: 700; font-size: 50px; letter-spacing: 2px;
  }

  .front__info { position: absolute; left: 0; top: 373px; width: 100%; }
  .person-name {
    position: absolute; top: 20px; width: 100%; text-align: center;
    font-weight: 600; font-size: 33px; letter-spacing: -0.5px;
    background: linear-gradient(90deg, var(--violet), var(--magenta));
    -webkit-background-clip: text; background-clip: text; color: transparent;
  }
  .person-role {
    position: absolute; top: 80px; width: 100%; text-align: center;
    color: var(--white); font-size: 21px; letter-spacing: 1px; font-weight: 400;
  }
  .divider {
    position: absolute; top: 339px; left: 98px; width: 256px; height: 1.5px;
    background: linear-gradient(90deg, var(--violet), var(--magenta));
  }
  .front__info .divider { top: 339px; }

  .contact-list { position: absolute; left: 90px; top: 365px; list-style: none; }
  .card--front > .contact-list { top: 507px; }
  .contact {
    display: flex; align-items: flex-start; gap: 12px;
    color: var(--white); font-size: 19.5px; line-height: 27px;
    margin-bottom: 11px;
  }
  .contact svg { flex: 0 0 26px; width: 26px; height: 26px; margin-top: 1px; }
</style>
</head>
<body>
<main class="stage">

  <section class="card card--back" aria-label="Card back">
    <div class="brand-vertical">TRIVELO</div>
  </section>

  <section class="card card--front" aria-label="Card front">
    <div class="front__brand-zone">
      <span class="brand-dot"></span>
      <span class="brand-name">TRIVELO</span>
    </div>

    <div class="front__info">
      <h1 class="person-name">FLORIAN GASTIER</h1>
      <p class="person-role">CO-FOUNDER &amp; CEO</p>
    </div>

    <div class="divider" style="top:712px; left:98px; width:256px; position:absolute;"></div>

    <ul class="contact-list">
      <li class="contact">
        <svg viewBox="0 0 24 24" aria-hidden="true"><path fill="#e3119c" d="M6.6 2.5c.6-.4 1.4-.3 1.8.3l2.3 3.3c.4.6.3 1.4-.2 1.8L9 9.2c.9 2.1 3.2 4.6 5.6 5.8l1.4-1.5c.5-.5 1.3-.6 1.9-.2l3.3 2.2c.6.4.8 1.2.4 1.8l-1.2 2c-.6 1-1.8 1.5-2.9 1.2C11 19 5 13 3.5 6.4c-.3-1.1.2-2.3 1.2-2.9z"/></svg>
        <span>(+33) 6 52 84 26 07</span>
      </li>
      <li class="contact">
        <svg viewBox="0 0 24 24" aria-hidden="true"><rect x="2" y="5" width="20" height="14" fill="#e3119c"/><path d="M2 5l10 8 10-8M2 19l7.5-7M22 19l-7.5-7" stroke="#05003c" stroke-width="1.5" fill="none"/></svg>
        <span>florian@trivelo.example</span>
      </li>
      <li class="contact">
        <svg viewBox="0 0 24 24" aria-hidden="true"><g fill="none" stroke="#9b10e8" stroke-width="1.6"><circle cx="12" cy="12" r="10"/><ellipse cx="12" cy="12" rx="4.5" ry="10"/><path d="M2 12h20M4 7h16M4 17h16M12 2v20"/></g></svg>
        <span>www.trivelo.example</span>
      </li>
      <li class="contact">
        <svg viewBox="0 0 24 24" aria-hidden="true"><path fill="#b010d8" d="M12 1.5a7.5 7.5 0 0 0-7.5 7.5c0 4.6 7.5 13.5 7.5 13.5S19.5 13.6 19.5 9A7.5 7.5 0 0 0 12 1.5zm0 11a3.6 3.6 0 1 1 0-7.2 3.6 3.6 0 0 1 0 7.2z"/></svg>
        <span>17 rue des Tanneurs<br>69001&nbsp; LYON</span>
      </li>
    </ul>
  </section>

</main>
</body>
</html>
```